Website for new dental office

I am Dr. Colin Marsh and am building a new dental practice. I specialize in general dentistry. I am young and have a higher end dental practice incorporating very new technologies and would like my website to reflect that. As many dental patients are older, the website must be very easy to navigate. I would like patients to be able to request appointments, and will eventually add on patient information forms (the health history, etc, that you normally fill out in the practice) from my practice management software, so leave an area for that.

Industry/Entity Type

Building

```html
<!DOCTYPE html>
<html lang="en">
<head>
<meta charset="utf-8">
<title>Colin Marsh DDS</title>
<link href="https://fonts.googleapis.com/css2?family=Lato:ital,wght@0,400;0,700;0,900;1,400&family=Open+Sans:wght@400;600&display=swap" rel="stylesheet">
<style>
:root{
  --blue:#1a73c0;
  --navy:#0d3658;
  --ink:#1e2a35;
  --text:#555b61;
  --orange:#f7a20d;
  --dark:#262626;
  --footer:#1b1b1b;
  --light:#f3f3f3;
  --line:#dcdcdc;
  --white:#ffffff;
}
*{margin:0;padding:0;box-sizing:border-box}
html,body{width:1200px;height:2558px;overflow:hidden}
body{position:relative;background:var(--white);font-family:"Open Sans",Arial,sans-serif;color:var(--text)}
.abs{position:absolute}
a{color:inherit;text-decoration:none}

/* top bar */
.topbar{left:0;top:0;width:1200px;height:36px;background:var(--dark);color:#ddd;font-size:13px}
.topbar .phone{left:132px;top:9px;display:flex;align-items:center;gap:10px}
.topbar nav{right:132px;top:9px;display:flex;gap:22px}

/* header */
.header{left:0;top:36px;width:1200px;height:96px;background:var(--white)}
.brand{left:130px;top:20px;font-family:"Lato",sans-serif;color:var(--blue);font-weight:700;line-height:1}
.brand .name{font-size:30px}
.brand .dds{font-size:15px;display:block;text-align:center;margin-top:2px;width:135px}
.mainnav{top:38px;left:0;width:1200px;font-family:"Lato",sans-serif;font-weight:700;font-size:16px;color:var(--ink);text-transform:uppercase}
.mainnav a{position:absolute}
.mainnav a.active{color:var(--blue)}

/* hero */
.hero{left:0;top:132px;width:1200px;height:524px;background:linear-gradient(180deg,#5bb6ea 0%,#a9d9f3 55%,#eaf5fb 100%)}
.hero-photo{left:500px;top:0;width:700px;height:524px;background:radial-gradient(ellipse at 55% 45%,#e8c0a0 0%,#d9ab88 35%,#e9d3a4 55%,rgba(240,230,200,0) 75%)}
.hero h1{left:132px;top:140px;font-family:"Lato",sans-serif;font-weight:400;font-size:31px;line-height:36px;color:var(--ink);text-transform:uppercase}
.btn-orange{background:var(--orange);color:var(--white);font-family:"Lato",sans-serif;font-size:15px;text-transform:uppercase;display:flex;align-items:center;justify-content:center}
.hero .btn-orange{left:132px;top:298px;width:153px;height:46px}

/* booking */
.booking{left:132px;top:588px;width:936px;height:137px;background:#2a2a2a}
.booking .label{left:0;top:0;width:174px;height:137px;background:var(--blue);color:var(--white);font-family:"Lato",sans-serif;font-weight:700;font-size:15px;text-align:center;text-transform:uppercase;line-height:19px;padding-top:82px}
.booking .label svg{position:absolute;left:71px;top:26px}
.field{background:var(--white);border-radius:3px;font-size:12px;color:#aaa;padding:12px 10px;height:41px}
.booking .submit{left:744px;top:17px;width:172px;height:100px;font-weight:900;line-height:20px;text-align:center;font-size:16px}

/* features */
.feature{top:778px;width:320px;text-align:center}
.feature h2{font-family:"Lato",sans-serif;font-weight:400;font-size:21px;color:var(--ink);margin-top:18px;text-transform:uppercase}
.feature .rule{width:40px;height:3px;background:var(--ink);margin:8px auto 12px}
.feature p{font-size:13px;line-height:21px;color:var(--text)}

/* welcome */
.welcome{left:0;top:1057px;width:1200px;height:452px;background:linear-gradient(180deg,var(--light),#fafafa 40%,var(--light))}
.welcome .intro{left:132px;top:55px;width:640px}
.welcome .kicker{font-family:"Lato",sans-serif;font-style:italic;font-size:19px;color:#555}
.welcome h2{font-family:"Lato",sans-serif;font-weight:700;font-size:24px;color:var(--blue);text-transform:uppercase;margin:2px 0 14px}
.welcome p{font-size:12.6px;line-height:21px;margin-bottom:12px;color:#666}
.welcome .more{color:var(--blue);font-size:12.6px;display:block;margin-top:6px}
.portrait{left:800px;top:30px;width:265px;height:340px;background:radial-gradient(ellipse at 50% 40%,#9a9a9a 0%,#c4c4c4 40%,rgba(250,250,250,0) 72%)}

/* news & gallery */
.section-title{font-family:"Lato",sans-serif;font-weight:700;font-size:19px;color:var(--ink);text-transform:uppercase}
.tag-more{background:var(--blue);color:var(--white);font-size:9px;padding:2px 6px;text-transform:uppercase}
.news{left:132px;top:1558px;width:286px}
.news .head,.gallery .head{display:flex;justify-content:space-between;align-items:center;border-bottom:1px solid var(--line);padding-bottom:10px}
.post{border-bottom:1px solid var(--line);padding:14px 0 14px}
.post .date{font-size:10.5px;color:#777}
.post h3{font-family:"Open Sans",sans-serif;font-weight:600;font-size:13.5px;color:var(--ink);margin:4px 0 6px}
.post p{font-size:12.6px;line-height:21px;color:#666}
.post:last-child{border-bottom:none}
.gallery{left:456px;top:1558px;width:612px}
.shots{position:absolute;left:0;top:55px;width:612px;height:177px}
.shot{position:absolute;top:0;width:148px;height:177px}
.pair-tag{position:absolute;width:44px;height:72px}

/* clients */
.clients{left:132px;top:1858px;width:936px;border-top:1px solid var(--line)}
.clients h2{position:absolute;left:0;top:58px;width:936px;text-align:center;font-family:"Lato",sans-serif;font-weight:400;font-size:21px;color:var(--ink);text-transform:uppercase}
.testimonial{left:132px;top:1960px;width:797px;height:167px;background:var(--white);box-shadow:0 0 10px rgba(0,0,0,.15)}
.testimonial .photo{left:0;top:0;width:145px;height:167px;background:linear-gradient(180deg,#1d5b95,#2d78bb)}
.testimonial p{left:166px;top:12px;width:580px;font-size:12.4px;line-height:21px;color:#555}
.testimonial .who{left:170px;top:132px;font-size:13px;color:var(--blue);font-weight:600}
.client-figure{left:912px;top:1871px;width:156px;height:277px;background:linear-gradient(180deg,rgba(233,233,233,0) 0%,#dfe3e7 25%,#c9d0d7 65%,#b9c2cb 100%)}

/* call band */
.callband{left:0;top:2148px;width:1200px;height:104px;background:var(--navy);color:var(--white);text-align:center;font-family:"Lato",sans-serif}
.callband .small{font-size:22px;padding-top:12px;line-height:26px}
.callband .big{font-size:44px;line-height:52px}

/* footer */
.footer{left:0;top:2252px;width:1200px;height:306px;background:linear-gradient(180deg,#232323,var(--footer));color:#cfcfcf;font-size:13px}
.footer h4{font-family:"Lato",sans-serif;font-weight:700;font-size:14px;color:var(--white);text-transform:uppercase;margin-bottom:10px}
.footer ul{list-style:none}
.footer li{line-height:26px}
.contact-row{display:flex;gap:16px;line-height:22px;margin-bottom:14px}
.contact-row .ic{width:30px;height:30px;border-radius:50%;background:#3a3a3a;flex:none;display:flex;align-items:center;justify-content:center}
.footer .bottom{left:132px;top:242px;width:936px;border-top:1px solid #333;padding-top:14px;display:flex;justify-content:space-between;font-size:12.5px}
.social{display:flex;gap:8px;margin-top:-6px}
.social span{width:28px;height:28px;border-radius:50%;background:#3a3a3a;display:block}
</style>
</head>
<body>

<div class="abs topbar">
  <div class="abs phone">
    <svg width="14" height="14" viewBox="0 0 24 24"><path fill="#ddd" d="M6.6 10.8a15.1 15.1 0 0 0 6.6 6.6l2.2-2.2c.3-.3.7-.4 1-.2 1.1.4 2.3.6 3.6.6.6 0 1 .4 1 1V20c0 .6-.4 1-1 1A17 17 0 0 1 3 4c0-.6.4-1 1-1h3.5c.6 0 1 .4 1 1 0 1.3.2 2.5.6 3.6.1.3 0 .7-.2 1z"/></svg>
    <span>(555) 0142-3867</span>
  </div>
  <nav class="abs"><a>Home</a><a>About Us</a><a>Patient Forms</a><a>Blog</a><a>Gallery</a><a>Contact Us</a></nav>
</div>

<header class="abs header">
  <div class="abs brand"><span class="name">Colin Marsh</span><span class="dds">DDS</span></div>
  <nav class="abs mainnav">
    <a class="active" style="left:438px">Restorative Dentistry</a>
    <a style="left:670px">Dentures</a>
    <a style="left:797px">Crowns &amp; Bridges</a>
    <a style="left:993px">Implants</a>
  </nav>
</header>

<section class="abs hero">
  <div class="abs hero-photo" role="img" aria-label="Smiling young couple posing together against a bright sky"></div>
  <h1 class="abs">Restructure<br>your outlook on life<br>with a brand new smile</h1>
  <a class="abs btn-orange">Learn More</a>
</section>

<section class="abs booking">
  <div class="abs label">
    <svg width="32" height="32" viewBox="0 0 32 32"><rect x="3" y="6" width="26" height="23" rx="2" fill="#fff"/><rect x="3" y="6" width="26" height="6" fill="#d8e8f6"/><rect x="9" y="2" width="3" height="7" fill="#fff"/><rect x="20" y="2" width="3" height="7" fill="#fff"/><g fill="#1a73c0"><rect x="7" y="15" width="4" height="3"/><rect x="14" y="15" width="4" height="3"/><rect x="21" y="15" width="4" height="3"/><rect x="7" y="21" width="4" height="3"/><rect x="14" y="21" width="4" height="3"/><rect x="21" y="21" width="4" height="3"/></g></svg>
    Book an<br>Appointment
  </div>
  <div class="abs field" style="left:192px;top:17px;width:258px">Full Name</div>
  <div class="abs field" style="left:469px;top:17px;width:258px">Phone Number</div>
  <div class="abs field" style="left:192px;top:77px;width:258px">Email Address</div>
  <div class="abs field" style="left:469px;top:77px;width:258px">Appointment Date</div>
  <a class="abs btn-orange submit">Make<br>Appointment</a>
</section>

<section class="abs feature" style="left:106px">
  <svg width="64" height="64" viewBox="0 0 64 64" fill="none" stroke="#1a73c0" stroke-width="4" stroke-linecap="round"><path d="M12 6v14a12 12 0 0 0 24 0V6"/><path d="M24 32v10a12 12 0 0 0 24 0v-8"/><circle cx="48" cy="28" r="6"/></svg>
  <h2>About Us</h2><div class="rule"></div>
  <p>We offer phenomenal dental treatments that<br>dramatically improve your overall health and<br>boost your self-esteem. Learn more about the<br>dentists who can provide them for you!</p>
</section>
<section class="abs feature" style="left:409px">
  <svg width="64" height="64" viewBox="0 0 64 64"><rect x="22" y="10" width="20" height="10" rx="3" fill="none" stroke="#1a73c0" stroke-width="4"/><rect x="6" y="18" width="52" height="38" rx="5" fill="#1a73c0"/><circle cx="32" cy="37" r="12" fill="#fff"/><path d="M32 30v14M25 37h14" stroke="#1a73c0" stroke-width="4"/></svg>
  <h2>SmileMill Dentistry</h2><div class="rule"></div>
  <p>Marsh Dental is the proud owner of a<br>state-of-the-art SmileMill machine, so our<br>in-office laboratory can craft you a brand new<br>smile during a single visit to our office.</p>
</section>
<section class="abs feature" style="left:763px">
  <svg width="64" height="64" viewBox="0 0 64 64"><circle cx="32" cy="32" r="26" fill="none" stroke="#1a73c0" stroke-width="5"/><path d="M24 25a8 8 0 1 1 11 7.4c-2 .9-3 2.2-3 4.6v3" fill="none" stroke="#1a73c0" stroke-width="5" stroke-linecap="round"/><circle cx="32" cy="47" r="3.2" fill="#1a73c0"/></svg>
  <h2>How Can We Help?</h2><div class="rule"></div>
  <p>Patient safety, health, and comfort are our<br>highest priorities as dental professionals.<br>Contact Marsh Dental today to schedule a<br>comprehensive examination.</p>
</section>

<section class="abs welcome">
  <div class="abs intro">
    <div class="kicker">Welcome to</div>
    <h2>Marsh Dental Cosmetic Dentistry-Lake Jackson</h2>
    <p>At Marsh Dental, our focus is on providing effective, comprehensive, and affordable cosmetic dentistry services to patients living in Lake Jackson, Brazosport, Angleton, and cities throughout Texas. Serving the Lone Star State for several decades, Marsh Dental has been one of the leading providers of restorative and cosmetic enhancement dentistry. Dr. Colin K. Marsh is a talented dentist who has dedicated his life to fulfilling patients' oral health needs and exceeding patients' expectations.</p>
    <p>At Marsh Dental, patients are treated like family. Focusing on patients' wellbeing, Dr. Colin Marsh educates his patients on restorative options, services that he can provide, and what to expect when undergoing treatment. By doing so, our dental team can successfully shape treatment plans for patients that yield premium results and amplify overall health.</p>
    <a class="more">[Read More...]</a>
  </div>
  <div class="abs portrait" role="img" aria-label="Black and white portrait of the dentist in shirt and tie"></div>
</section>

<section class="abs news">
  <div class="head"><span class="section-title">Latest News</span><span class="tag-more">More</span></div>
  <article class="post"><div class="date">June 2014 Post</div><h3>Lorem Ipsum is simply dummy text</h3><p>Lorem Ipsum is simply dummy text of all a<br>the printing and typesetting industry.</p></article>
  <article class="post"><div class="date">June 2014 Post</div><h3>Lorem Ipsum is simply dummy text</h3><p>Lorem Ipsum is simply dummy text of all a<br>the printing and typesetting industry.</p></article>
</section>

<section class="abs gallery">
  <div class="head"><span class="section-title">Smile Gallery</span><span class="tag-more">More</span></div>
  <div class="shots">
    <div class="shot" style="left:0;background:linear-gradient(135deg,#d8b49a,#c99a7f)" role="img" aria-label="Patient smile before treatment"></div>
    <div class="shot" style="left:153px;background:linear-gradient(135deg,#e8c6b0,#d5a288)" role="img" aria-label="Patient smile after treatment"></div>
    <div class="shot" style="left:311px;background:linear-gradient(135deg,#c99a74,#a87a58)" role="img" aria-label="Second patient smile before treatment"></div>
    <div class="shot" style="left:464px;background:linear-gradient(135deg,#e7b89c,#c4704f)" role="img" aria-label="Second patient smile after treatment"></div>
    <svg class="pair-tag" style="left:130px;top:38px" viewBox="0 0 44 72"><rect x="4" y="6" width="36" height="16" fill="#1a73c0" transform="rotate(-35 22 14)"/><text x="22" y="19" fill="#fff" font-family="Lato,sans-serif" font-size="10" font-weight="700" text-anchor="middle" transform="rotate(-35 22 14)">After</text><rect x="4" y="46" width="36" height="16" fill="#1a73c0" transform="rotate(-35 22 54)"/><text x="22" y="58" fill="#fff" font-family="Lato,sans-serif" font-size="10" font-weight="700" text-anchor="middle" transform="rotate(-35 22 54)">Before</text></svg>
    <svg class="pair-tag" style="left:441px;top:38px" viewBox="0 0 44 72"><rect x="4" y="6" width="36" height="16" fill="#1a73c0" transform="rotate(-35 22 14)"/><text x="22" y="19" fill="#fff" font-family="Lato,sans-serif" font-size="10" font-weight="700" text-anchor="middle" transform="rotate(-35 22 14)">After</text><rect x="4" y="46" width="36" height="16" fill="#1a73c0" transform="rotate(-35 22 54)"/><text x="22" y="58" fill="#fff" font-family="Lato,sans-serif" font-size="10" font-weight="700" text-anchor="middle" transform="rotate(-35 22 54)">Before</text></svg>
  </div>
</section>

<section class="abs clients"><h2>Happy Clients</h2></section>
<div class="abs testimonial">
  <div class="abs photo" role="img" aria-label="Portrait of a smiling client wearing glasses"></div>
  <p class="abs">Lorem ipsum dolor sit amet, consectetur adipisicing elit, sed do eiusmod tempor incididunt ut labore et dolore magna aliqua. Ut enim ad minim veniam, quis nostrud exercitation ullamco laboris nisi ut aliquip ex ea commodo consequat. Duis aute irure dolor in reprehenderit in voluptate velit esse cillum dolore eu fugiat nulla pariatur. Excepteur sint occaecat cupidatat non proident.</p>
  <div class="abs who">-Clients Name Here</div>
</div>
<div class="abs client-figure" role="img" aria-label="Standing client in glasses and shirt"></div>

<section class="abs callband">
  <div class="small">Call Now For a Free</div>
  <div class="big">(555) 0142-3867 &nbsp;/&nbsp; info@colinmarshdds.com</div>
</section>

<footer class="abs footer">
  <div class="abs" style="left:132px;top:40px">
    <h4>Quick Links</h4>
    <ul><li>Home</li><li>About Us</li><li>Restorative Dentistry</li><li>Cosmetic Dentistry</li><li>Managing Dental Phobia</li></ul>
  </div>
  <div class="abs" style="left:365px;top:64px">
    <ul><li>Contact Us</li><li>Gallery</li><li>Site Map</li><li>Patient Information Form</li><li>Dental History Form</li></ul>
  </div>
  <div class="abs" style="left:600px;top:40px;width:300px">
    <h4 style="margin-left:40px">Get in Touch</h4>
    <div class="contact-row"><span class="ic"><svg width="12" height="16" viewBox="0 0 12 16"><path fill="#ddd" d="M6 0a6 6 0 0 0-6 6c0 4.5 6 10 6 10s6-5.5 6-10a6 6 0 0 0-6-6zm0 8.5A2.5 2.5 0 1 1 6 3.5a2.5 2.5 0 0 1 0 5z"/></svg></span><span>Marsh Dental Colin Marsh, DDS<br>Lake Jackson Office 240 Cedar<br>Bend Drive Lake Jackson, TX 77566</span></div>
    <div class="contact-row"><span class="ic"><svg width="13" height="13" viewBox="0 0 24 24"><path fill="#ddd" d="M6.6 10.8a15.1 15.1 0 0 0 6.6 6.6l2.2-2.2c.3-.3.7-.4 1-.2 1.1.4 2.3.6 3.6.6.6 0 1 .4 1 1V20c0 .6-.4 1-1 1A17 17 0 0 1 3 4c0-.6.4-1 1-1h3.5c.6 0 1 .4 1 1 0 1.3.2 2.5.6 3.6.1.3 0 .7-.2 1z"/></svg></span><span style="line-height:30px">(555) 0142-3867</span></div>
  </div>
  <div class="abs" style="left:934px;top:40px">
    <h4>Procedures</h4>
    <ul><li>Restorative Dentistry</li><li>Dentures</li><li>Crowns &amp; Bridges</li><li>Implants</li></ul>
  </div>
  <div class="abs bottom">
    <span>© 2014 Marsh Dental Colin Marsh, DDS. &nbsp; Privacy Policy &nbsp; Terms and Conditions</span>
    <div class="social"><span></span><span></span><span></span></div>
  </div>
</footer>

</body>
</html>
```